DRIFTFRAME studio

Design to be modern with colours of logo, maybe orange background. Include name, position, phone/WhatsApp email/web. Specialises in long form TIMELAPSE

Contact Information for Business Card

Marcel Okoro, filmmaker,/photographer, phone/WhatsApp +971529386047, email - marcel@driftframestudio.com www.driftframestudio.com, instagram @driftframestudio

Font styles to use
Sans Serif

Requirements
Must have
• Fresh, bright, modern, original
Marcel Okoro - Filmmaker/Photographer
Phone/WhatsApp +971 529 38 6047
email - marcel@driftfarmestudio.com
Web - driftfarmestudio.com
PoBox 584319, Dubai, UAE
instagram - driftframestudio
Should not have
• solid black background

```html
<!DOCTYPE html>
<html lang="en">
<head>
<meta charset="utf-8">
<title>DRIFTFRAME studio – Business Card</title>
<link rel="stylesheet" href="https://fonts.googleapis.com/css2?family=Arimo:wght@400;700&display=swap">
<style>
  :root {
    --backdrop: #c0c1c3;
    --orange: #f48835;
    --orange-deep: #cb6d2b;
    --ink: #3b3b3b;
    --black: #000000;
    --white: #ffffff;
  }
  html, body {
    margin: 0;
    padding: 0;
    width: 1200px;
    height: 764px;
    overflow: hidden;
    background: var(--backdrop);
    font-family: "Arimo", Arial, sans-serif;
  }
  .card {
    position: absolute;
    left: 89px;
    top: 82px;
    width: 1021px;
    height: 598px;
    background: var(--orange);
    overflow: hidden;
  }
  .card-shapes {
    position: absolute;
    inset: 0;
  }
  .brand {
    position: absolute;
    left: 560px;
    top: 62px;
    display: flex;
    align-items: center;
    gap: 16px;
  }
  .brand-dot {
    width: 34px;
    height: 34px;
    border-radius: 50%;
    background: var(--orange);
  }
  .brand-name {
    margin: 0;
    color: var(--orange);
    font-weight: 700;
    font-size: 40px;
    letter-spacing: 0.5px;
    white-space: nowrap;
  }
  .person-name {
    position: absolute;
    left: 40px;
    top: 92px;
    margin: 0;
    color: var(--ink);
    font-weight: 700;
    font-size: 48px;
    letter-spacing: 0.5px;
    line-height: 1;
    white-space: nowrap;
  }
  .name-rule {
    position: absolute;
    left: 0;
    top: 148px;
    width: 450px;
    height: 4px;
    background: var(--white);
  }
  .person-role {
    position: absolute;
    left: 40px;
    top: 172px;
    margin: 0;
    color: var(--ink);
    font-size: 28px;
    line-height: 1;
  }
  .contact-list {
    position: absolute;
    left: 42px;
    top: 0;
    margin: 0;
    padding: 0;
    list-style: none;
  }
  .contact-item {
    position: absolute;
    left: 0;
    display: flex;
    align-items: center;
    gap: 17px;
    color: var(--ink);
    font-size: 26px;
    white-space: nowrap;
    transform: translateY(-50%);
  }
  .contact-item.phone { top: 424px; }
  .contact-item.email { top: 454px; }
  .contact-item.web { top: 517px; }
  .contact-item.social { top: 557px; }
  .contact-icon {
    width: 20px;
    height: 20px;
    flex: none;
  }
</style>
</head>
<body>
  <main class="card">
    <svg class="card-shapes" width="1021" height="598" viewBox="0 0 1021 598" aria-hidden="true">
      <polygon class="panel-deep" points="604,0 1021,0 1021,598 442,598" fill="var(--orange-deep)"/>
      <polygon class="top-tab" points="432,0 550,0 536,40 437,12" fill="var(--orange-deep)"/>
      <polygon class="brand-panel" points="550,0 1021,0 1021,191 508,191" fill="var(--black)"/>
      <polyline class="brand-edge" points="536,45 498,197 1010,197" fill="none" stroke="var(--white)" stroke-width="5"/>
    </svg>

    <div class="brand">
      <span class="brand-dot"></span>
      <p class="brand-name">DRIFTFRAME studio</p>
    </div>

    <h1 class="person-name">MARCEL OKORO</h1>
    <div class="name-rule"></div>
    <p class="person-role">filmmaker,/photographer</p>

    <ul class="contact-list">
      <li class="contact-item phone">
        <svg class="contact-icon" viewBox="0 0 20 20" aria-hidden="true">
          <circle cx="10" cy="10" r="10" fill="var(--ink)"/>
          <path d="M6.5 5.2l1.8-.4 1 2.4-1.1.9c.6 1.4 1.6 2.4 3 3l.9-1.1 2.4 1-.4 1.8c-4.2.4-8-3.4-7.6-7.6z" fill="var(--white)"/>
        </svg>
        <span>+971529386047</span>
      </li>
      <li class="contact-item email">
        <svg class="contact-icon" viewBox="0 0 20 20" aria-hidden="true">
          <circle cx="10" cy="10" r="10" fill="var(--ink)"/>
          <rect x="5" y="6.5" width="10" height="7" fill="var(--white)"/>
          <polyline points="5,6.5 10,10.5 15,6.5" fill="none" stroke="var(--ink)" stroke-width="1"/>
        </svg>
        <span>marcel@driftframestudio.com</span>
      </li>
      <li class="contact-item web">
        <svg class="contact-icon" viewBox="0 0 20 20" aria-hidden="true">
          <circle cx="10" cy="10" r="10" fill="var(--ink)"/>
          <g fill="none" stroke="var(--white)" stroke-width="1">
            <circle cx="10" cy="10" r="5.5"/>
            <ellipse cx="10" cy="10" rx="2.3" ry="5.5"/>
            <line x1="4.5" y1="10" x2="15.5" y2="10"/>
          </g>
        </svg>
        <span>www.driftframestudio.com</span>
      </li>
      <li class="contact-item social">
        <svg class="contact-icon" viewBox="0 0 20 20" aria-hidden="true">
          <circle cx="10" cy="10" r="10" fill="var(--ink)"/>
        </svg>
        <span>@driftframestudio</span>
      </li>
    </ul>
  </main>
</body>
</html>
```